Tu Vois Scène (Masterclasses for Actors) needs artistic and modern website in French & English

Hello!

We need to create a new website (existing : www.tu-vois-scene.example) for our acting school that holds Masterclasses for professional actors in Paris. It needs to be in French and English with an easy to use back office (wordpress is slow and complicated) (ideas?) so we can add or change workshop dates, upload new photos or videos to the gallery ourselves and make basic changes to the information on line.

Our main clients are French but we have international guests coming who only understand english.

Ideally you would know how to link your creation to the existing domain name, how to make sure the email adresses remain the same and help us find the least expensive but best all in 1 proposition to make it as easy as possible to pay the yearly fee to the hosting platform / web name / etc :-)

Design wise we would like something creative, linked to films etc but without using to many clichés. The logo and a stamp have already been created and we would like to keep these (which has the colours we would like you to use).

It would be nice to maybe have a moving image when you first open the page, maybe the logo itself, something dynamic and visual...

Thank you for you time in reading this!

Margaux & Noémie & Camille
Team TVS

Target Market(s)

actors

Coding

Coded - Design and coding required

Number of Pages Required

5+ page

Font styles to use
Sans Serif

Colors
34a7d8

Requirements
Must have
• able to be read on all electronic devices
Nice to have
• some fun and humour / class
Should not have
• too corporate

```html
<!DOCTYPE html>
<html lang="en">
<head>
<meta charset="utf-8">
<title>Tu Vois Scène — Masterclasses for Actors</title>
<link href="https://fonts.googleapis.com/css2?family=Oswald:wght@400;500&family=Open+Sans:ital,wght@0,400;0,600;1,400&display=swap" rel="stylesheet">
<style>
:root{
  --brand:#34a7d8;
  --brand-deep:#3a80c0;
  --gold:#e0b43c;
  --accent-red:#d9262b;
  --ink:#333;
  --muted:#777;
  --light:#f0f0f0;
  --footer:#121316;
  --white:#fff;
}
*{box-sizing:border-box;margin:0;padding:0}
html,body{width:1200px;height:3261px;overflow:hidden}
body{position:relative;font-family:"Open Sans",Arial,sans-serif;color:var(--ink);background:var(--white)}
.abs{position:absolute}
h1,h2,h3,.nav,.logo-name{font-family:"Oswald","Arial Narrow",sans-serif;font-weight:400}

/* hero */
.hero{position:absolute;left:0;top:0;width:1200px;height:678px;overflow:hidden}
.hero-photo{position:absolute;inset:0;background:linear-gradient(180deg,#2a3a4a 0%,#3f4c55 25%,#8a6a40 52%,#c7822f 60%,#5a3a1c 75%,#201408 100%)}
.logo{left:98px;top:72px;color:var(--white);text-align:center}
.logo-name{font-size:38px;letter-spacing:1px;line-height:1;display:block}
.logo-tag{font-size:10px;letter-spacing:2px;display:block;margin-top:8px}
.phone{left:772px;top:36px;color:var(--white);font-family:"Oswald",sans-serif;font-size:18px;display:flex;align-items:center;gap:10px}
.lang{left:996px;top:33px;width:104px;height:34px;border:1px solid rgba(255,255,255,.6);border-radius:3px;color:var(--white);font-size:10px;display:flex;align-items:center;justify-content:center;gap:6px;background:rgba(0,0,0,.2)}
.flag{width:16px;height:10px;background:#2a4c9a;display:inline-block}
.nav{left:435px;top:87px;width:665px;height:35px;display:flex;justify-content:space-between;align-items:center;color:var(--white);font-size:13px;text-transform:uppercase}
.nav a{color:inherit;text-decoration:none;padding:0 4px}
.nav .active{background:var(--brand-deep);border-radius:18px;padding:8px 22px}
.hero-title{left:0;width:1200px;top:328px;text-align:center;color:var(--white);font-size:52px;font-weight:500}
.hero-sub{left:0;width:1200px;top:398px;text-align:center;color:var(--white);font-size:14px;font-weight:600;letter-spacing:.5px;line-height:22px;text-transform:uppercase}
.dots{left:566px;top:466px;display:flex;gap:8px}
.dots i{width:10px;height:10px;border-radius:50%;background:var(--white);display:block}
.dots i.on{box-shadow:0 0 0 3px rgba(255,255,255,.5)}

/* welcome */
.sec-title{left:0;width:1200px;text-align:center;font-size:40px}
.welcome-title{top:732px;color:var(--brand-deep)}
.welcome-text{left:152px;width:896px;top:796px;text-align:center;font-size:11.5px;line-height:19px;color:var(--muted)}
.feature{width:330px;text-align:center}
.feature-icon{width:128px;height:128px;border-radius:50%;border:5px solid var(--gold);margin:0 auto;display:flex;align-items:center;justify-content:center;background:var(--white)}
.feature-icon span{width:104px;height:104px;border-radius:50%;background:var(--brand-deep);display:flex;align-items:center;justify-content:center}
.feature h3{font-size:22px;margin-top:22px;color:#222}
.feature p{font-size:11.5px;line-height:19px;color:var(--muted);margin-top:6px;padding:0 12px}

/* videos */
.videos{left:0;top:1211px;width:1200px;height:500px;background:linear-gradient(180deg,#ececec,#f4f4f4)}
.videos-title{top:1262px;color:var(--ink)}
.rule{height:3px}
.video{width:315px;height:215px;overflow:hidden}
.video-photo{position:absolute;inset:0}
.video-bar{position:absolute;left:0;top:0;width:100%;height:34px;background:rgba(0,0,0,.55);color:var(--white);font-size:11px;padding:9px 14px;display:flex;justify-content:space-between}
.play{position:absolute;left:50%;top:50%;transform:translate(-50%,-38%)}
.video-cap{font-family:"Oswald",sans-serif;font-size:17px;color:var(--ink)}

/* portfolio */
.portfolio-title{top:1763px;color:var(--ink)}
.filter{top:1862px;font-family:"Oswald",sans-serif;font-size:17px;color:var(--ink)}
.filter.on{border:1px solid var(--brand);border-radius:16px;width:70px;height:30px;text-align:center;line-height:28px;top:1861px}
.tile{overflow:hidden}
.tile-feature{background:var(--brand-deep);color:var(--white);text-align:center;padding-top:46px}
.tile-feature h3{font-size:27px}
.tile-feature p{font-size:11.5px;line-height:17px;width:320px;margin:10px auto 0}
.tile-btn{display:inline-block;margin-top:14px;border:1px solid var(--white);font-size:12px;font-weight:600;padding:5px 14px}

/* testimonial */
.quote-band{left:0;top:2500px;width:1200px;height:385px;background:linear-gradient(90deg,#5c4638 0%,#8c7a6c 25%,#d9d9d9 45%,#f4f4f4 60%,#f6f6f6 100%)}
.quote-mark{left:788px;top:2565px;font-family:"Oswald",sans-serif;font-size:150px;line-height:1;color:#2c2c2c}
.quote-text{left:515px;width:581px;top:2672px;text-align:center;font-size:11.5px;line-height:19px;color:#555}
.quote-by{left:515px;width:581px;top:2745px;text-align:center;font-style:italic;font-size:17px;color:#444}
.quote-dots{left:752px;top:2798px;display:flex;gap:6px}
.quote-dots i{width:28px;height:3px;background:#bbb;display:block}
.quote-dots i.on{background:#333}

/* footer */
.footer{left:0;top:2885px;width:1200px;height:376px;background:linear-gradient(180deg,#1b1d22,var(--footer))}
.stamp{left:98px;top:2918px;width:164px;height:164px;border-radius:50%;background:var(--white);border:8px solid var(--gold);box-shadow:inset 0 0 0 18px var(--brand-deep)}
.socials{left:106px;top:3106px;display:flex;gap:6px}
.socials i{width:28px;height:28px;border-radius:50%;border:2px solid #ccc;display:block}
.f-head{font-family:"Oswald",sans-serif;font-size:17px;color:var(--white)}
.f-text{font-size:12px;line-height:20px;color:#ddd}
.contact-row{left:341px;display:flex;gap:18px;align-items:flex-start}
.field{left:680px;top:3039px;width:242px;height:40px;background:var(--white);font-size:11px;color:#777;padding:12px 10px}
.subscribe{left:680px;top:3096px;width:101px;height:38px;background:var(--brand-deep);color:var(--white);font-size:11px;font-weight:600;text-align:center;line-height:38px}
.links{left:996px;top:2988px;list-style:none}
.links li{font-size:12px;color:#ddd;line-height:25px}
.links li::before{content:"›";margin-right:8px}
.copy-rule{left:0;top:3196px;width:1200px;height:1px;background:#2c2e33}
.copy{left:0;width:1200px;top:3216px;text-align:center;font-size:11px;color:#ccc}
</style>
</head>
<body>

<header class="hero">
  <div class="hero-photo" role="img" aria-label="Silhouettes of a film crew with a boom microphone and camera against a sunset field"></div>
  <div class="abs logo"><span class="logo-name">TU VOIS SCÈNE</span><span class="logo-tag">CREATIVE • CINEMA • TRAINING</span></div>
  <div class="abs phone">
    <svg width="18" height="18" viewBox="0 0 24 24"><path fill="#fff" d="M6.6 10.8a15 15 0 0 0 6.6 6.6l2.2-2.2c.3-.3.7-.4 1-.2 1.1.4 2.3.6 3.6.6.6 0 1 .4 1 1V20c0 .6-.4 1-1 1A17 17 0 0 1 3 4c0-.6.4-1 1-1h3.5c.6 0 1 .4 1 1 0 1.3.2 2.5.6 3.6.1.3 0 .7-.2 1z"/></svg>
    Call us +33 6 00 00 00 00
  </div>
  <div class="abs lang"><i class="flag"></i>ENGLISH ▾</div>
  <nav class="abs nav">
    <a class="active">Home</a><a>About</a><a>Stages</a><a>Photos</a><a>Videos</a><a>Events</a><a>The Team</a><a>Partners</a><a>Blog</a><a>Contacts</a>
  </nav>
  <h1 class="abs hero-title">TU VOIS SCÈNE</h1>
  <p class="abs hero-sub">We are an acting school that holds masterclasses for<br>professional actors in Paris.</p>
  <div class="abs dots"><i class="on"></i><i></i><i></i><i></i></div>
</header>

<section>
  <h2 class="abs sec-title welcome-title">Welcome To Tu Vois Scène</h2>
  <p class="abs welcome-text">Sed ut perspiciatis unde omnis iste natus error sit voluptatem accusantium doloremque laudantium, totam rem aperiam, eaque ipsa quae ab illo inventore veritatis et quasi architecto beatae vitae dicta sunt explicabo. Nemo enim ipsam voluptatem quia voluptas sit aspernatur aut odit aut fugit, sed quia consequuntur magni dolores eos qui ratione voluptatem sequi nesciunt. Neque porro quisquam est, qui dolorem ipsum quia dolor sit amet, consectetur, adipisci velit, sed quia non numquam.</p>

  <div class="abs feature" style="left:105px;top:896px">
    <div class="feature-icon"><span><svg width="46" height="46" viewBox="0 0 24 24" fill="none" stroke="#fff" stroke-width="1.6"><rect x="3" y="4" width="18" height="12" rx="1"/><path d="M8 20h8M12 16v4"/></svg></span></div>
    <h3>CREATIVE</h3>
    <p>Lorem ipsum dolor sit amet, consectetur adipiscing elit, sed do eiusmod tempor incididunt ut labore et dolore magna aliqua. Ut enim ad minim veniam</p>
  </div>
  <div class="abs feature" style="left:446px;top:896px">
    <div class="feature-icon"><span><svg width="46" height="46" viewBox="0 0 24 24" fill="none" stroke="#fff" stroke-width="1.6"><rect x="4" y="10" width="16" height="10" rx="1"/><path d="M4 10l15-4 1 3-15 4zM9 8.7l2 3M14 7.4l2 3"/></svg></span></div>
    <h3>CINEMA</h3>
    <p>Lorem ipsum dolor sit amet, consectetur adipiscing elit, sed do eiusmod tempor incididunt ut labore et dolore magna aliqua. Ut enim ad minim veniam</p>
  </div>
  <div class="abs feature" style="left:789px;top:896px">
    <div class="feature-icon"><span><svg width="46" height="46" viewBox="0 0 24 24" fill="none" stroke="#fff" stroke-width="1.6"><path d="M3 5c3 1 6 1 9 0v6c0 3-2 5-4.5 5S3 14 3 11z"/><path d="M12 9c3 1 6 1 9 0v6c0 3-2 5-4.5 5S12 18 12 15"/></svg></span></div>
    <h3>TRAINING</h3>
    <p>Lorem ipsum dolor sit amet, consectetur adipiscing elit, sed do eiusmod tempor incididunt ut labore et dolore magna aliqua. Ut enim ad minim veniam</p>
  </div>
</section>

<section>
  <div class="abs videos"></div>
  <h2 class="abs sec-title videos-title">Here Is How It Looks Like</h2>
  <div class="abs rule" style="left:557px;top:1323px;width:86px;background:var(--accent-red)"></div>

  <div class="abs video" style="left:98px;top:1383px">
    <div class="video-photo" role="img" aria-label="Video still of an actress rehearsing a scene in a studio" style="background:linear-gradient(135deg,#6a3a30,#b04a4a 50%,#3a2a2a)"></div>
    <div class="video-bar"><span>TVS STAGE à la campagne 2011</span><span>⋖</span></div>
    <svg class="play" width="52" height="38" viewBox="0 0 52 38"><rect width="52" height="38" rx="9" fill="rgba(0,0,0,.6)"/><path d="M21 11l12 8-12 8z" fill="#fff"/></svg>
  </div>
  <div class="abs video" style="left:443px;top:1383px">
    <div class="video-photo" role="img" aria-label="Video still of an actor performing a monologue" style="background:linear-gradient(135deg,#2a3a6a,#5a6a9a 50%,#20284a)"></div>
    <div class="video-bar"><span>TVS : Jean Dorval English Monologue</span><span>⋖</span></div>
    <svg class="play" width="52" height="38" viewBox="0 0 52 38"><rect width="52" height="38" rx="9" fill="rgba(0,0,0,.6)"/><path d="M21 11l12 8-12 8z" fill="#fff"/></svg>
  </div>
  <div class="abs video" style="left:785px;top:1383px">
    <div class="video-photo" role="img" aria-label="Video still of a performer filmed outdoors among bamboo" style="background:linear-gradient(135deg,#2f4a2a,#5a7a4a 50%,#2a3a22)"></div>
    <div class="video-bar"><span>Creations des comediens</span><span>⋖</span></div>
    <svg class="play" width="52" height="38" viewBox="0 0 52 38"><rect width="52" height="38" rx="9" fill="rgba(0,0,0,.6)"/><path d="M21 11l12 8-12 8z" fill="#fff"/></svg>
  </div>
  <p class="abs video-cap" style="left:98px;top:1612px">Clip Presentation</p>
  <p class="abs video-cap" style="left:443px;top:1612px">Monologue</p>
  <p class="abs video-cap" style="left:785px;top:1612px">Creations des comediens</p>
</section>

<section>
  <h2 class="abs sec-title portfolio-title">Our Portfolio</h2>
  <div class="abs rule" style="left:560px;top:1828px;width:80px;height:2px;background:var(--brand)"></div>
  <span class="abs filter on" style="left:389px">All</span>
  <span class="abs filter" style="left:481px">Coaching</span>
  <span class="abs filter" style="left:567px">Lieu</span>
  <span class="abs filter" style="left:621px">Soirees networking</span>
  <span class="abs filter" style="left:771px">Stages</span>

  <div class="abs tile tile-feature" style="left:98px;top:1933px;width:433px;height:237px">
    <h3>Soirees Networking</h3>
    <p>Sed ut perspiciatis unde omnis iste natus error sit voluptatem accusantium doloremque Sed ut perspiciatis unde omnis iste natus</p>
    <span class="tile-btn">VIEW DETAILS</span>
  </div>
  <div class="abs tile" role="img" aria-label="Crew filming beside a pool under an umbrella" style="left:539px;top:1933px;width:276px;height:237px;background:linear-gradient(160deg,#8a9a8a,#5a7a9a 60%,#4a5a4a)"></div>
  <div class="abs tile" role="img" aria-label="Group of actors gathered in a sunny garden" style="left:824px;top:1933px;width:276px;height:237px;background:linear-gradient(160deg,#6a7a3a,#a08a4a 50%,#3a4a2a)"></div>
  <div class="abs tile" role="img" aria-label="Outdoor shoot with a red umbrella and camera crew" style="left:98px;top:2178px;width:267px;height:237px;background:linear-gradient(160deg,#4a5a3a,#8a3a3a 45%,#3a4030)"></div>
  <div class="abs tile" role="img" aria-label="Actors working around a table in a rehearsal room" style="left:376px;top:2178px;width:268px;height:237px;background:linear-gradient(160deg,#7a5a3a,#b0906a 50%,#4a3a2a)"></div>
  <div class="abs tile" role="img" aria-label="Audience watching a screening in a dim stone room" style="left:652px;top:2178px;width:448px;height:237px;background:radial-gradient(ellipse at 30% 30%,#c89a50,#6a4a2a 50%,#241810)"></div>
</section>

<section>
  <div class="abs quote-band" role="img" aria-label="Camera operator holding a stabilised film camera on set"></div>
  <div class="abs quote-mark">”</div>
  <p class="abs quote-text">Lorem ipsum dolor sit amet, consectetur adipiscing elit, sed do eiusmod tempor incididunt ut labore et dolore magna aliqua. Ut enim ad minim veniam, quis nostrud exercitation ullamco laboris nisi ut aliquip ex ea commodo consequat. Duis aute irure dolor in reprehenderit in voluptate velit esse cillum</p>
  <p class="abs quote-by">Our comedian (ne) s talk about Tu Vois Scène</p>
  <div class="abs quote-dots"><i class="on"></i><i></i><i></i></div>
</section>

<footer>
  <div class="abs footer"></div>
  <div class="abs stamp"></div>
  <div class="abs socials"><i></i><i></i><i></i><i></i></div>

  <h3 class="abs f-head" style="left:341px;top:2946px">CONTACT US</h3>
  <div class="abs contact-row f-text" style="top:3003px">
    <svg width="14" height="18" viewBox="0 0 24 30" fill="none" stroke="#ddd" stroke-width="2"><path d="M12 28S3 17 3 11a9 9 0 0 1 18 0c0 6-9 17-9 17z"/><circle cx="12" cy="11" r="3"/></svg>
    <span>TU VOIS SCÈNE 12 Rue des Coulisses<br>Paris 75011</span>
  </div>
  <div class="abs contact-row f-text" style="top:3053px">
    <svg width="16" height="16" viewBox="0 0 24 24" fill="none" stroke="#ddd" stroke-width="2"><path d="M6.6 10.8a15 15 0 0 0 6.6 6.6l2.2-2.2 4.6 1.2V20A17 17 0 0 1 4 4h3.6l1.2 4.6z"/></svg>
    <span>Phone : +33 6 00 00 00 00</span>
  </div>
  <div class="abs contact-row f-text" style="top:3086px">
    <svg width="16" height="14" viewBox="0 0 24 18" fill="none" stroke="#ddd" stroke-width="2"><rect x="1" y="1" width="22" height="16"/><path d="M1 1l11 9 11-9"/></svg>
    <span>Email: contact@tu-vois-scene.example</span>
  </div>

  <h3 class="abs f-head" style="left:680px;top:2946px">JOIN OUR NEWSLETTER</h3>
  <p class="abs f-text" style="left:680px;top:2986px;width:250px;font-size:11.5px">Excepteur sint occaecat cupidatat non proident, sunt in culpa qui</p>
  <div class="abs field">Enter Name</div>
  <div class="abs subscribe">SUBSCRIBE</div>

  <h3 class="abs f-head" style="left:996px;top:2946px">QUICK LINKS</h3>
  <ul class="abs links">
    <li>About</li><li>Stages</li><li>Photos</li><li>Videos</li><li>Events</li><li>The team</li><li>PartnersBlog</li>
  </ul>

  <div class="abs copy-rule"></div>
  <p class="abs copy">Copyright 2016 | All Rights Reserved – TU VOIS SCÈNE</p>
</footer>

</body>
</html>
```